Flyer for Daycare

A Flyer for family group daycare
Specfs:
- One side english / Another Side spanish(the text for both sides is below)
- The flyer is for printing in 5" x 7" or 5.5" x 8.5"
- The address and phone number is the most important
Logo(see the attachment)
NYC Licensed
Children from 6 Weeks to 12 years old
Accepting All the Programs( BWD, OFT) and Private
CPR & First Aid Certified
Full Time, Part Time and After School
----------------------------------------------------------------------------
Provide Homework Assistance
Potty Training
Outdoor Activities
Nutritional Meals & Snack
Baby Wipes
Text in Spanish
Licencia por el estado de NY
Niños de 6 semanas a 12 años
Aceptando Todos los Programas (BWD, OFT) y Privado
Certificación en CPR y Primeros Auxilios
Tiempo completo, tiempo parcial y después de la escuela
----------------------------------------------------------------------------------------------
Actividades al aire libre
Asistencia con la tarea
Entrenamiento para ir al baño
Desayunos, Comidas y refrigerios nutricionales
Toallitas para bebé
382 E 514th ST
APT 4C
Bronx, NY, 10758
ig: @velomarkdaycare
555-318-7704
LAtin and Black, Bronx NY Area
Daycare service

```html
<!DOCTYPE html>
<html lang="en">
<head>
<meta charset="utf-8">
<title>Velomark Day Care Flyer</title>
<link rel="stylesheet" href="https://fonts.googleapis.com/css2?family=Fredoka:wght@500;600;700&display=swap">
<style>
  :root {
    --green: #1f8a10;
    --navy: #1717a3;
    --red: #f40000;
    --white: #ffffff;
    --wood: #eba472;
    --wood-dark: #5a2b16;
    --post: #4b2a1c;
    --orange: #ff8a00;
    --yellow: #ffec00;
    --sky: #4dd6ff;
    --leaf: #1e9a0a;
    --purple: #a315c9;
  }
  html, body { margin: 0; padding: 0; overflow: hidden; background: #fff; }
  .flyer {
    position: relative; width: 776px; height: 1200px; overflow: hidden;
    background: var(--white);
    font-family: "Fredoka", sans-serif;
  }
  .hero-photo {
    position: absolute; left: 0; top: 0; width: 776px; height: 392px;
    background: linear-gradient(100deg, #d9d4c8 0%, #cfc9bd 35%, #f1ece6 60%, #e8ddd0 100%);
  }
  .decor { position: absolute; left: 0; top: 0; }
  .brand {
    position: absolute; left: 14px; top: 338px; width: 292px; height: 205px;
    background: var(--white); border-radius: 110px 120px 100px 90px;
    display: flex; align-items: center; justify-content: center; gap: 10px;
  }
  .brand-dot { width: 26px; height: 26px; border-radius: 50%; background: var(--navy); }
  .brand-name {
    color: var(--navy); font-weight: 700; font-size: 30px; line-height: 1.05; text-align: center;
  }
  .headline {
    position: absolute; left: 318px; top: 440px; width: 426px; margin: 0;
    text-align: center; color: var(--green); font-weight: 700; font-size: 38px; line-height: 48px;
    white-space: nowrap;
  }
  .facts {
    position: absolute; left: 0; top: 550px; width: 776px; margin: 0; padding: 0;
    list-style: none; text-align: center; color: var(--navy); font-weight: 600; font-size: 26.5px; line-height: 37.5px;
    white-space: nowrap;
  }
  .service {
    position: absolute; width: 158px; height: 166px;
    background: var(--red); border-radius: 48% 52% 44% 56% / 55% 45% 55% 45%;
    display: flex; align-items: center; justify-content: center; text-align: center;
    color: var(--white); font-weight: 700; font-size: 22px; line-height: 30px;
    box-shadow: 4px 3px 0 -1px #fff, 6px 5px 0 0 var(--red);
  }
  .post { position: absolute; width: 26px; background: var(--post); }
  .sign {
    position: absolute; background: var(--wood); color: var(--wood-dark);
    font-weight: 600; text-align: center; box-sizing: border-box;
  }
  .sign-address {
    left: 226px; top: 1020px; width: 266px; height: 136px; transform: rotate(-3deg);
    font-size: 28px; line-height: 34px; padding-top: 10px; white-space: nowrap;
  }
  .sign-contact {
    left: 520px; top: 1026px; width: 236px; height: 112px; transform: rotate(4deg);
    font-size: 19px; line-height: 40px; padding: 14px 0 0 16px; text-align: left; white-space: nowrap;
  }
  .contact-row { display: flex; align-items: center; gap: 8px; }
  .handle-mark { width: 22px; height: 22px; background: var(--post); border-radius: 6px; flex: none; }
</style>
</head>
<body>
<main class="flyer">
  <div class="hero-photo" role="img" aria-label="Photo of two toddlers playing with colourful stacking toys in a bright playroom"></div>

  <svg class="decor" width="776" height="1200" viewBox="0 0 776 1200" aria-hidden="true">
    <path d="M0 390 H776 V415 C700 430 640 400 560 420 C480 380 420 420 300 395 L0 395Z" fill="var(--yellow)"/>
    <path d="M310 392 C330 420 370 425 400 400 Z" fill="var(--sky)"/>
    <path d="M630 414 C640 390 720 388 730 414 Z" fill="var(--leaf)"/>
    <path d="M0 392 H40 C60 450 40 520 0 555 Z" fill="var(--orange)"/>
    <path d="M0 560 C60 570 60 650 40 690 L0 690 Z" fill="var(--sky)"/>
    <path d="M0 708 C40 660 90 690 92 708 Z" fill="var(--yellow)"/>
    <path d="M0 790 C60 840 50 920 0 965 Z" fill="var(--sky)"/>
    <ellipse cx="35" cy="530" rx="22" ry="14" fill="var(--purple)"/>
    <path d="M776 470 C690 520 690 640 776 680 V640 C730 610 730 540 776 510 Z" fill="var(--leaf)"/>
    <path d="M776 510 C740 540 740 600 776 640 Z" fill="var(--yellow)"/>
    <path d="M776 770 C730 790 730 860 776 880 Z" fill="var(--leaf)"/>
    <path d="M0 1015 C50 1020 70 1100 60 1200 H0 Z" fill="var(--orange)"/>
    <ellipse cx="62" cy="1065" rx="26" ry="18" fill="var(--yellow)"/>
    <path d="M776 995 C740 1030 740 1120 776 1150 Z" fill="var(--purple)"/>
  </svg>

  <div class="brand">
    <span class="brand-dot"></span>
    <span class="brand-name">Velomark<br>Day Care</span>
  </div>

  <h1 class="headline">Where Your Little Angel<br>Can Grow and Learn</h1>

  <ul class="facts">
    <li>NYC Licensed</li>
    <li>Children from 6 Weeks to 12 years old</li>
    <li>Accepting All the Programs( BWD, OFT) and Private</li>
    <li>CPR &amp; First Aid Certified</li>
    <li>Full Time, Part Time and After School</li>
  </ul>

  <div class="service" style="left:38px;top:747px;">Provide<br>Homework<br>Assistance</div>
  <div class="service" style="left:172px;top:838px;">Potty<br>Training</div>
  <div class="service" style="left:315px;top:758px;">Outdoor<br>Activities</div>
  <div class="service" style="left:461px;top:843px;">Baby<br>Wipes</div>
  <div class="service" style="left:593px;top:743px;">Nutritional<br>Meals &amp;<br>Snack</div>

  <div class="post" style="left:349px;top:995px;height:205px;"></div>
  <div class="post" style="left:610px;top:1005px;height:195px;"></div>

  <div class="sign sign-address">382 E 514th ST<br>APT 4C<br>Bronx, NY, 10758</div>

  <div class="sign sign-contact">
    <div class="contact-row"><span class="handle-mark"></span>@velomarkdaycare</div>
    <div class="contact-row">
      <svg width="22" height="22" viewBox="0 0 24 24" aria-hidden="true"><path d="M6.6 10.8a15 15 0 0 0 6.6 6.6l2.2-2.2a1 1 0 0 1 1-.25 11.4 11.4 0 0 0 3.6.57 1 1 0 0 1 1 1V20a1 1 0 0 1-1 1A17 17 0 0 1 3 4a1 1 0 0 1 1-1h3.5a1 1 0 0 1 1 1c0 1.25.2 2.45.57 3.57a1 1 0 0 1-.25 1Z" fill="var(--post)"/></svg>
      555-318-7704
    </div>
  </div>
</main>
</body>
</html>
```